New Zealand Luggage Importer Needs Business Cards

We need professional, creative and fashionable business cards created.
We are based in New Zealand and import and distribute high-end, quality, fashionable and durable luggage.
We pride ourselves on selling the very best quality luggage, second only to 1 brand (which we won't mention here)...we use the same manufacturer. However, our prices are much more reasonable.
Industry/Entity Type
Business
Contact Information for Business Card
Mark Dunsley
027 512 4068
3/17 Harlow Street, Pinecrest Flats, Auckland, 0614
PO Box 204377, Fernside, Auckland 0731
09-528-3916
sales@brivancases.co.nz / www.brivancases.co.nz

```html
<!DOCTYPE html>
<html lang="en">
<head>
<meta charset="UTF-8">
<title>Brivan Cases — Business Cards</title>
<link href="https://fonts.googleapis.com/css2?family=Montserrat:wght@400;700&family=Open+Sans:wght@300;400;600&display=swap" rel="stylesheet">
<style>
  :root {
    --backdrop: #3a3a3c;
    --card: #121213;
    --card-edge: #1c1c1e;
    --logo-tone: #4a4a4d;
    --gold: #c9a95a;
    --white: #f4f4f4;
    --soft: #b9b9bb;
    --rule: #6c6c6e;
  }
  * { box-sizing: border-box; margin: 0; padding: 0; }
  html, body { width: 1200px; height: 1000px; overflow: hidden; }
  body {
    background: var(--backdrop);
    position: relative;
    font-family: "Open Sans", Arial, sans-serif;
  }
  .card {
    position: absolute;
    width: 630px;
    height: 360px;
    background: var(--card);
    border: 1px solid var(--card-edge);
    border-radius: 22px;
    box-shadow: 0 18px 40px rgba(0,0,0,.45);
  }
  .card--front { left: 90px; top: 90px; }
  .card--back { left: 480px; top: 550px; }

  .brand-name {
    position: absolute;
    left: 0; right: 0; top: 140px;
    text-align: center;
    font-family: "Open Sans", Arial, sans-serif;
    font-weight: 600;
    font-size: 46px;
    letter-spacing: 4px;
    color: var(--logo-tone);
  }
  .front-web {
    position: absolute;
    left: 0; right: 0; bottom: 38px;
    text-align: center;
    font-size: 14px;
    letter-spacing: 3px;
    color: var(--soft);
  }
  .front-web .accent, .contact-web .accent { color: var(--gold); }

  .identity {
    position: absolute;
    left: 60px; top: 120px;
    text-align: right;
  }
  .person-name {
    font-family: "Montserrat", Arial, sans-serif;
    font-size: 30px;
    line-height: 1;
    white-space: nowrap;
  }
  .person-name .first { color: var(--white); font-weight: 700; }
  .person-name .last { color: var(--gold); font-weight: 400; }
  .person-role {
    margin-top: 6px;
    font-size: 15px;
    color: var(--white);
  }
  .divider {
    position: absolute;
    left: 335px; top: 92px;
    width: 1px; height: 100px;
    background: var(--rule);
  }
  .contact-list {
    position: absolute;
    left: 352px; top: 92px;
    list-style: none;
  }
  .contact-list li {
    display: flex;
    align-items: center;
    gap: 10px;
    height: 25px;
    font-size: 15px;
    color: var(--soft);
    white-space: nowrap;
  }
  .contact-list svg { width: 12px; height: 12px; flex: none; }
  .address {
    position: absolute;
    right: 40px; bottom: 38px;
    text-align: right;
    font-size: 15px;
    line-height: 1.4;
    color: var(--soft);
  }
</style>
</head>
<body>

<section class="card card--front" aria-label="Card front">
  <div class="brand-name">BRIVAN CASES</div>
  <div class="front-web">www.<span class="accent">brivancases</span>.co.nz</div>
</section>

<section class="card card--back" aria-label="Card back">
  <div class="identity">
    <div class="person-name"><span class="first">MARK</span> <span class="last">DUNSLEY</span></div>
    <div class="person-role">Owner</div>
  </div>
  <div class="divider"></div>
  <ul class="contact-list">
    <li>
      <svg viewBox="0 0 12 12" aria-hidden="true"><path d="M2.5 1 L4.5 1 L5 3.5 L3.8 4.3 Q5 6.8 7.7 8.2 L8.5 7 L11 7.5 L11 9.5 Q10.5 11 9 11 Q1 10 1 2.5 Q1 1 2.5 1Z" fill="var(--gold)"/></svg>
      027 512 4068
    </li>
    <li>
      <svg viewBox="0 0 12 12" aria-hidden="true"><path d="M1 4 Q6 0.5 11 4 L10 5.5 L8.3 4.8 L8.3 4 Q6 3 3.7 4 L3.7 4.8 L2 5.5Z" fill="var(--gold)"/><rect x="2.5" y="6" width="7" height="5" rx="1" fill="var(--gold)"/><circle cx="6" cy="8.5" r="1.2" fill="var(--card)"/></svg>
      09-528-3916
    </li>
    <li>
      <svg viewBox="0 0 12 12" aria-hidden="true"><path d="M1 5.5 L11 1 L7 11 L5.8 6.6Z" fill="none" stroke="var(--gold)" stroke-width="1.2" stroke-linejoin="round"/></svg>
      sales@brivancases.co.nz
    </li>
    <li class="contact-web">
      <svg viewBox="0 0 12 12" aria-hidden="true"><circle cx="7" cy="5" r="3.6" fill="none" stroke="var(--gold)" stroke-width="1.3"/><path d="M4.4 7.6 L1 11" stroke="var(--gold)" stroke-width="1.6" stroke-linecap="round"/></svg>
      <span>www.<span class="accent">brivancases</span>.co.nz</span>
    </li>
  </ul>
  <div class="address">
    3/17 Harlow Street, Pinecrest Flats, Auckland, 0614<br>
    PO Box 204377, Fernside, Auckland 0731
  </div>
</section>

</body>
</html>
```